Non fiction leadership Book Cover design needed for “Keep Bold: Begin Owning Daily”

I need a front cover design for a new book 6 X 9 traditional non-fiction book.

Title: "Keep BOLD - Begin Owning Daily"

The subtitle is not finalized- so use 2 lines of smaller dummy text

My brand guide is attached (please use the tan color sparingly)

I'd like to see BOLD look like it is in motion and "flying" across the page

Need CREATIVE designs and options

Do not want my picture on the front cover - I do want it on the back cover.

On the front cover I’d like to see creative use of font to create movement on “BOLD”

Target Market(s)

Business leaders

Industry/Entity Type

Aviation

Font styles to use
Other font styles liked:
• See style guide- can add additional font (modern script or san serif)

Colors
0054AA
0677BA
7BADD7
CADEEF
E8F1F8
EB3D1F
EC4F4E
F09395
F8D3D4
FCEDEE

Requirements
Must have
• Creative font use, using perspective to create movement/motion on BOLD
Should not have
• My picture on the front cover- my picture should be on the back cover

```html
<!DOCTYPE html>
<html lang="en">
<head>
<meta charset="utf-8">
<title>Keep Bold: Begin Owning Daily — Front Cover</title>
<link rel="stylesheet" href="https://fonts.googleapis.com/css2?family=Josefin+Sans:wght@200;300&family=Inter:wght@400;800&display=swap">
<style>
  :root {
    --page-bg: #2b2b2d;
    --cover-blue-light: #4a82be;
    --cover-blue: #346fb0;
    --cover-blue-deep: #1f5599;
    --ink-line: #ebece6;
    --ink-type: #f2f3f0;
    --art-tint-top: rgba(235, 236, 230, 0.10);
    --art-tint-bottom: rgba(235, 236, 230, 0.03);
  }

  * { box-sizing: border-box; margin: 0; padding: 0; }

  html, body {
    width: 1200px;
    height: 900px;
    overflow: hidden;
    background: var(--page-bg);
  }

  .book-cover {
    position: absolute;
    left: 310px;
    top: 42px;
    width: 580px;
    height: 816px;
    overflow: hidden;
    background: linear-gradient(160deg, var(--cover-blue-light) 0%, var(--cover-blue) 45%, var(--cover-blue-deep) 100%);
  }

  .cage-artwork {
    position: absolute;
    left: 150px;
    top: 0;
    width: 310px;
    height: 610px;
  }

  .title-lettering {
    position: absolute;
    left: 110px;
    top: 250px;
    font-family: "Josefin Sans", sans-serif;
    font-weight: 200;
    color: var(--ink-type);
    text-transform: uppercase;
    line-height: 1;
  }

  .title-lettering__keep {
    display: block;
    font-size: 96px;
    letter-spacing: 2px;
    transform: rotate(9deg);
    transform-origin: left center;
  }

  .title-lettering__bold {
    display: block;
    margin-top: 34px;
    margin-left: 54px;
    font-size: 88px;
    letter-spacing: 4px;
    transform: rotate(9deg) skewX(-8deg);
    transform-origin: left center;
  }

  .title-tagline {
    position: absolute;
    left: 222px;
    top: 548px;
    font-family: "Josefin Sans", sans-serif;
    font-weight: 300;
    font-size: 22px;
    letter-spacing: 0.5px;
    color: var(--ink-type);
    text-transform: uppercase;
    transform: rotate(-22deg);
    transform-origin: left bottom;
    white-space: nowrap;
  }

  .title-orbit {
    position: absolute;
    left: 140px;
    top: 470px;
    width: 380px;
    height: 140px;
  }

  .subtitle {
    position: absolute;
    left: 0;
    right: 0;
    top: 711px;
    text-align: center;
    font-family: "Inter", sans-serif;
    color: var(--ink-type);
    text-transform: uppercase;
  }

  .subtitle__line {
    display: block;
    font-size: 13px;
    line-height: 21px;
    letter-spacing: 0.4px;
  }

  .subtitle__line--first { font-weight: 400; }
  .subtitle__line--second { font-weight: 800; }
</style>
</head>
<body>
  <main class="book-cover">
    <svg class="cage-artwork" viewBox="0 0 310 610" role="img"
         aria-label="Line-drawn open birdcage whose falling bars turn into the title lettering">
      <defs>
        <linearGradient id="cageTint" x1="0" y1="0" x2="0" y2="1">
          <stop offset="0" stop-color="var(--art-tint-top)"/>
          <stop offset="1" stop-color="var(--art-tint-bottom)"/>
        </linearGradient>
      </defs>
      <rect x="0" y="0" width="310" height="610" rx="18" fill="url(#cageTint)"/>
    </svg>

    <svg class="title-orbit" viewBox="0 0 380 140" aria-hidden="true">
      <ellipse cx="190" cy="72" rx="178" ry="34" transform="rotate(-12 190 72)"
               fill="none" stroke="var(--ink-line)" stroke-width="2.5"/>
    </svg>

    <h1 class="title-lettering">
      <span class="title-lettering__keep">Keep</span>
      <span class="title-lettering__bold">Bold</span>
    </h1>

    <p class="title-tagline">Begin Owning Daily</p>

    <p class="subtitle">
      <span class="subtitle__line subtitle__line--first">The subtitle is not finalized-</span>
      <span class="subtitle__line subtitle__line--second">So use 2 lines of smaller dummy text</span>
    </p>
  </main>
</body>
</html>
```